Business Cards for a Junk Removal Company

Hello,
We are looking to have business cards designed that are simple, bold, easy to read, and right to the point. Please see the attachments for our logo files. We want the card to be yellow on both sides ( Color code Yellow: #FFE01B). The logo text font is (Rockstar Extra Bold) and this is also in the files attached. Please make the text black for the logo. On the back side of the card, you can use white and black for text. Thank you in advance for your hard work!

Front of card-
Harbor Haul Away (logo)
Back of card-
Harbor Haul Away
Donate - Recycle - Dispose
555-271-8093
www.harborhaulaway.example
info@harborhaulaway.example

Industry/Entity Type

Junk removal

Contact Information for Business Card

FRONT OF CARD- Harbor Haul Away (logo) BACK OF CARD- Harbor Haul Away Donate - Recycle - Dispose 555-271-8093 www.harborhaulaway.example info@harborhaulaway.example

Font styles to use
Other font styles liked:
• Rockstar Extra Bold

Colors
FFF300
FFF600
FEFA6F
FFFEC7
FFFEE8

Requirements
Must have
• Must have color code Yellow: #FFE01B for the background of front and back of the card

```html
<!DOCTYPE html>
<html lang="en">
<head>
<meta charset="utf-8">
<title>Harbor Haul Away — Business Cards</title>
<link rel="stylesheet" href="https://fonts.googleapis.com/css2?family=Anton&family=Oswald:wght@500;600&display=swap">
<style>
  :root {
    --card-yellow: #FFE01B;
    --ink: #111111;
    --backdrop: #d8d3ca;
    --shadow: rgba(0, 0, 0, 0.22);
  }
  * { box-sizing: border-box; margin: 0; padding: 0; }
  html, body {
    width: 1200px;
    height: 1023px;
    overflow: hidden;
  }
  body {
    background: var(--backdrop);
    position: relative;
    color: var(--ink);
  }
  .card {
    position: absolute;
    left: 290px;
    width: 620px;
    height: 354px;
    background: var(--card-yellow);
    box-shadow: 0 10px 28px var(--shadow);
  }
  .card--back { top: 110px; display: flex; flex-direction: column; }
  .card--front { top: 560px; display: flex; flex-direction: column; align-items: center; justify-content: center; }

  .brand-name {
    font-family: "Anton", "Arial Narrow", sans-serif;
    font-weight: 400;
    color: var(--ink);
    text-transform: uppercase;
    letter-spacing: 1px;
    line-height: 1;
  }

  /* back side bands */
  .band { display: flex; align-items: center; justify-content: center; }
  .band--logo { height: 150px; }
  .band--logo .brand-name { font-size: 60px; }
  .band--tagline {
    height: 74px;
    border-top: 1.5px solid var(--ink);
    border-bottom: 1.5px solid var(--ink);
  }
  .tagline {
    font-family: "Anton", "Arial Narrow", sans-serif;
    font-size: 38px;
    letter-spacing: 1px;
    text-transform: uppercase;
  }
  .band--contact {
    flex: 1;
    flex-direction: column;
    gap: 4px;
    font-family: "Oswald", "Arial Narrow", sans-serif;
  }
  .contact-phone {
    display: flex; align-items: center; gap: 10px;
    font-size: 30px; font-weight: 600; letter-spacing: 1px;
  }
  .contact-phone svg { width: 24px; height: 24px; }
  .contact-web, .contact-email { font-size: 23px; font-weight: 500; letter-spacing: 0.5px; }

  /* front side */
  .card--front .brand-name { font-size: 66px; }
  .front-web {
    margin-top: 26px;
    font-family: "Oswald", "Arial Narrow", sans-serif;
    font-weight: 500;
    font-size: 19px;
    letter-spacing: 3px;
    text-transform: uppercase;
  }
</style>
</head>
<body>
  <section class="card card--back" aria-label="Business card, contact side">
    <div class="band band--logo">
      <h1 class="brand-name">Harbor Haul Away</h1>
    </div>
    <div class="band band--tagline">
      <p class="tagline">Donate - Recycle - Dispose</p>
    </div>
    <div class="band band--contact">
      <p class="contact-phone">
        <svg viewBox="0 0 24 24" aria-hidden="true">
          <rect x="1" y="1" width="22" height="22" rx="4" fill="#111111"/>
          <path d="M8.2 5.5l2 2.6-1.3 1.5c.8 1.9 2.2 3.3 4.1 4.1l1.5-1.3 2.6 2-1.1 2.4c-4.9-.3-9-4.4-9.3-9.3z" fill="#FFE01B"/>
        </svg>
        555-271-8093
      </p>
      <p class="contact-web">www.harborhaulaway.example</p>
      <p class="contact-email">info@harborhaulaway.example</p>
    </div>
  </section>

  <section class="card card--front" aria-label="Business card, logo side">
    <h2 class="brand-name">Harbor Haul Away</h2>
    <p class="front-web">www.harborhaulaway.example</p>
  </section>
</body>
</html>
```